New travel store signage for Kelvane Journeys to attract luxury travellers.

Hello,
We are looking to change the signage of our stores. The signage must include the following:
1. Kelvane Journeys Logo (attached)
2. The text...The Travel & Cruise Experts
3. Brand Colours ( Fb0196, 412266, d41d84 and ffffff)
Please note the signage design must be central and only cover two thirds of the store front. We have also attached an image of one of our new stores which might be helpful when preparing a mock up.

We are looking for a quick turnaround on this, making a decision within 48 hours.

Target Market(s)

Retail

Industry/Entity Type

Travel Agency

Font styles to use
Other font styles liked:
• Radley

Colors
E54698
E96AAD
F1A4CE
F9D9EA
FCEFF6
6B429C
8869AF
B7A5CE
E3DAEB
F3F0F8

Requirements
Must have
• Hello, We are looking to change the signage of our stores. The signage must include the following: 1. Kelvane Journeys Logo (attached) 2. The text...The Travel & Cruise Experts 3. Brand Colours ( Fb0196, 412266, d41d84 and ffffff) Please note the signage design must be central and only cover two thirds of the store front.
Should not have
• different colour or fonts. Gradient design.

```html
<!DOCTYPE html>
<html lang="en">
<head>
<meta charset="utf-8">
<title>Kelvane Journeys – Store Signage</title>
<link rel="stylesheet" href="https://fonts.googleapis.com/css2?family=Montserrat:ital,wght@0,600;1,600&display=swap">
<style>
  :root {
    --navy: #412266;
    --navy-deep: #272163;
    --pink: #e6228a;
    --pink-deep: #d41d84;
    --white: #ffffff;
    --backdrop: #b3b3b3;
  }
  * { margin: 0; padding: 0; box-sizing: border-box; }
  html, body {
    width: 1200px;
    height: 1020px;
    overflow: hidden;
    background: var(--backdrop);
  }
  .canvas {
    position: relative;
    width: 1200px;
    height: 1020px;
  }
  .sign {
    position: absolute;
    overflow: hidden;
  }
  .sign svg {
    position: absolute;
    inset: 0;
    width: 100%;
    height: 100%;
    display: block;
  }
  .sign--fascia {
    left: 20px;
    top: 203px;
    width: 1161px;
    height: 275px;
  }
  .sign--panel {
    left: 338px;
    top: 623px;
    width: 540px;
    height: 300px;
  }
  .brand-name {
    position: absolute;
    display: flex;
    align-items: center;
    gap: 14px;
    font-family: "Montserrat", sans-serif;
    font-weight: 600;
    color: var(--navy-deep);
    white-space: nowrap;
    transform: translateX(-50%);
  }
  .brand-name__dot {
    border-radius: 50%;
    background: var(--pink);
    flex: none;
  }
  .sign--fascia .brand-name {
    left: 580px;
    top: 104px;
    font-size: 46px;
  }
  .sign--fascia .brand-name__dot { width: 26px; height: 26px; }
  .sign--panel .brand-name {
    left: 320px;
    top: 124px;
    font-size: 34px;
    gap: 10px;
  }
  .sign--panel .brand-name__dot { width: 20px; height: 20px; }
  .tagline {
    position: absolute;
    left: 580px;
    top: 222px;
    transform: translateX(-50%);
    font-family: "Montserrat", sans-serif;
    font-style: italic;
    font-weight: 600;
    font-size: 24px;
    color: var(--navy-deep);
    white-space: nowrap;
  }
</style>
</head>
<body>
<div class="canvas">

  <section class="sign sign--fascia">
    <svg viewBox="0 0 1935 459" preserveAspectRatio="none" aria-hidden="true">
      <rect width="1935" height="459" fill="var(--navy-deep)"/>
      <path fill="var(--white)" d="M507,0 L1829,0 C1850,60 1840,220 1700,320 C1600,390 1480,440 1400,459 L102,459 C102,230 250,60 507,0 Z"/>
      <path fill="var(--pink)" d="M530,0 L1807,0 C1825,60 1815,215 1680,315 C1580,385 1470,440 1412,459 L127,459 C127,240 280,70 530,0 Z"/>
      <path fill="var(--white)" d="M562,0 L1757,0 C1775,80 1760,220 1640,315 C1560,380 1460,435 1415,459 L179,459 C179,250 320,80 562,0 Z"/>
    </svg>
    <div class="brand-name"><span class="brand-name__dot"></span>Kelvane Journeys</div>
    <p class="tagline">The Travel &amp; Cruise Experts</p>
  </section>

  <section class="sign sign--panel">
    <svg viewBox="0 0 900 500" preserveAspectRatio="none" aria-hidden="true">
      <rect width="900" height="500" fill="var(--navy-deep)"/>
      <path fill="var(--white)" d="M73,0 L900,0 L900,500 L560,500 C420,480 300,440 220,380 C110,300 60,160 73,0 Z"/>
      <path fill="var(--pink)" d="M93,0 L900,0 L900,500 L575,500 C440,480 320,440 240,375 C135,295 85,160 93,0 Z"/>
      <path fill="var(--white)" d="M151,0 L900,0 L900,500 L591,500 C460,478 350,430 280,370 C180,285 140,160 151,0 Z"/>
    </svg>
    <div class="brand-name"><span class="brand-name__dot"></span>Kelvane Journeys</div>
  </section>

</div>
</body>
</html>
```